Velvet Chews Bottle Label- a psychedelic trippy mushroom brand

Velvet Chews is made out of the psychedelic Amanita mushroom that enhances one's reality and sends you on a trip. This is the most universally identifiable mushroom (red with white dots). This brand’s identity is trippy, psychedelic, fun and escapism.
The Velvet Chews logo will be placed on gummy bottles and gummy bags that will be sold online through an ecommerce webpage, social media campaigns and on shelves in retail stores. This is a fun label, have a blast with this!

- Logo should incorporate the Amanita mushroom either literally or in some trippy/psychedelic representation.
- Logo should be fun to look at sober, and trippy (a blast) to look at after you've taken the product
- Logo should invoke a mushroom effect. Examples of “the mushroom effect” below:
--- Mostly it’s just glowing colors, distortions, details popping out…good vibes
--- an explosion of stimuli, my mind zipped through so many connections
--- Your sense of time and space perception will be warped
colors appear to glow
--- You’ll notice surfaces glittering and an increased richness in texture of (all) things.
--- You may find yourself smiling uncontrollably, or feeling especially giggly.
--- First feelings are usually those of euphoria and an "opening up" of the world where colors become more vivid and solid objects appear to "breathe."
(see attached word doc for example logos in the industry)

Target Market(s)

Easy going crowd who are comfortable with taking mushrooms and look forward to having a good trip. They are easy going and not uptight.

Industry/Entity Type

Psychedelic Mushrooms

```html
<!DOCTYPE html>
<html lang="en">
<head>
<meta charset="utf-8">
<title>Mushroom Gummies Chaga Label</title>
<link rel="stylesheet" href="https://fonts.googleapis.com/css2?family=Chango&family=Bowlby+One&display=swap">
<style>
  :root {
    --ink: #0b0b0b;
    --paper: #ffffff;
    --navy: #1b2a8c;
    --cyan: #2fd3d8;
    --orange: #f2814f;
    --magenta: #e021c4;
    --night: #0a0614;
  }
  * { margin: 0; padding: 0; box-sizing: border-box; }
  html, body { width: 1200px; height: 614px; overflow: hidden; background: var(--paper); }
  .label {
    position: relative;
    width: 1200px;
    height: 614px;
    overflow: hidden;
    font-family: "Chango", "Bowlby One", sans-serif;
    background: var(--paper);
  }
  .artwork {
    position: absolute;
    left: 0; top: 0;
    width: 1200px; height: 547px;
    background:
      radial-gradient(circle at 12% 20%, rgba(255,80,200,.55), transparent 22%),
      radial-gradient(circle at 30% 70%, rgba(60,230,140,.5), transparent 24%),
      radial-gradient(circle at 85% 30%, rgba(255,200,40,.5), transparent 22%),
      radial-gradient(circle at 70% 78%, rgba(80,140,255,.5), transparent 24%),
      radial-gradient(circle at 50% 40%, rgba(170,80,255,.35), transparent 30%),
      var(--night);
  }
  .logo-badge {
    position: absolute;
    left: 520px; top: 28px;
    width: 186px; height: 184px;
    border-radius: 50%;
    background: var(--paper);
    display: flex; align-items: center; justify-content: center;
    text-align: center;
    color: var(--ink);
    font-size: 38px;
    line-height: 1.05;
  }
  .count-tab {
    position: absolute;
    left: 823px; top: -8px;
    width: 154px; height: 165px;
    background: var(--paper);
    border: 7px solid var(--cyan);
    border-top: none;
    border-radius: 0 0 30px 30px;
    text-align: center;
    color: var(--navy);
    padding-top: 24px;
  }
  .count-tab .count { display: block; font-size: 66px; line-height: 1; }
  .count-tab .unit { display: block; font-size: 16px; letter-spacing: 1px; margin-top: 4px; }
  .outlined {
    -webkit-text-stroke: 14px var(--paper);
    paint-order: stroke fill;
  }
  .product-title {
    position: absolute;
    left: 0; width: 1200px;
    top: 232px;
    text-align: center;
    color: var(--orange);
    font-size: 62px;
    line-height: 64px;
  }
  .variety {
    position: absolute;
    left: 0; width: 1200px;
    top: 388px;
    text-align: center;
    color: var(--navy);
    font-size: 54px;
    line-height: 60px;
  }
  .flavor {
    position: absolute;
    left: 0; width: 1200px;
    top: 455px;
    text-align: center;
    color: var(--magenta);
    font-size: 24px;
    line-height: 30px;
    -webkit-text-stroke: 8px var(--paper);
    paint-order: stroke fill;
  }
  .dose-tab {
    position: absolute;
    left: 271px; top: 457px;
    width: 158px; height: 170px;
    background: var(--paper);
    border: 7px solid var(--cyan);
    border-bottom: none;
    border-radius: 30px 30px 0 0;
    text-align: center;
    color: var(--navy);
    padding-top: 56px;
  }
  .dose-tab .dose { display: block; font-size: 26px; line-height: 1.1; }
  .dose-tab .per { display: block; font-size: 15px; margin-top: 6px; }
  .fine-print {
    position: absolute;
    left: 0; width: 1200px;
    text-align: center;
    color: var(--ink);
    font-family: "Bowlby One", sans-serif;
  }
  .fine-print.natural { top: 557px; font-size: 11px; }
  .fine-print.net { top: 582px; font-size: 16px; }
</style>
</head>
<body>
  <main class="label">
    <div class="artwork" role="img" aria-label="Psychedelic pattern of glowing rainbow neon mushrooms and stars on a black background"></div>

    <div class="logo-badge">YOUR<br>LOGO</div>

    <div class="count-tab">
      <span class="count">30</span>
      <span class="unit">GUMMIES</span>
    </div>

    <h1 class="product-title outlined">MUSHROOM<br>GUMMIES</h1>
    <h2 class="variety outlined">CHAGA</h2>
    <p class="flavor">BLACK RASPBERRY</p>

    <div class="dose-tab">
      <span class="dose">2500 MG</span>
      <span class="per">PER GUMMY</span>
    </div>

    <p class="fine-print natural">NATURAL FLAVOR</p>
    <p class="fine-print net">NET WT. = 476 OZ/(135G)</p>
  </main>
</body>
</html>
```